My Web Development Portfolio site

I'm a web developer and I need a web design that can showcase my web development portfolio. I like most of the websites from this link: http://www.mintquarry.example/galleries/samples-493051. My ideal design should be modern, clean and fun. I will let the designer decided the color theme for the website.

Target Market(s)

Potential Employers.

Number of Pages Required

1 page

Requirements
Must have
• - Menu bar that includes at least: About Me, Blog, Contact, Project/Work
• - Excellent color theme
• - Use the logo I provided (see attachment)
Nice to have
• - Some animation
• - Fun yet modern design

```html
<!DOCTYPE html>
<html lang="en">
<head>
<meta charset="utf-8">
<title>Jhon Doe — Front End Developer</title>
<link href="https://fonts.googleapis.com/css2?family=Mr+Dafoe&family=Questrial&display=swap" rel="stylesheet">
<style>
  :root {
    --paper: #f1f0f0;
    --hill: #e2e1e1;
    --nav-bg: #e4e3e3;
    --ink: #3a3a3a;
    --rust: #c4501a;
    --arc-outer: #f47f45;
    --arc-inner: #f2ac86;
    --blue: #0f67fb;
    --cyan: #0fd3f8;
    --green: #77bb00;
    --orange: #d04a10;
    --purple: #a21cf7;
    --pink: #fe1f76;
    --white: #ffffff;
  }
  html, body { margin: 0; padding: 0; overflow: hidden; background: var(--paper); }
  .canvas {
    position: relative; width: 1200px; height: 675px; overflow: hidden;
    background: var(--paper); font-family: "Questrial", sans-serif; color: var(--ink);
  }
  .backdrop { position: absolute; inset: 0; }
  .name {
    position: absolute; left: 128px; top: 70px; margin: 0;
    font-family: "Mr Dafoe", cursive; font-weight: 400; font-size: 76px;
    color: var(--rust); line-height: 1;
  }
  .intro {
    position: absolute; left: 135px; top: 171px; width: 726px; margin: 0;
    font-size: 15.5px; line-height: 22.5px; text-align: justify; color: var(--ink);
  }
  .skills { position: absolute; left: 0; top: 0; width: 1200px; height: 675px; }
  .skill {
    position: absolute; border-radius: 50%; color: var(--white);
    display: flex; flex-direction: column; align-items: center; justify-content: center;
    font-size: 16px;
  }
  .skill .label { margin-top: 10px; }
  .skill--awards { left: 77px; top: 412px; width: 164px; height: 164px; background: var(--blue); z-index: 1; }
  .skill--web { left: 209px; top: 412px; width: 164px; height: 164px; background: var(--cyan); z-index: 2; }
  .skill--css { left: 486px; top: 412px; width: 164px; height: 164px; background: var(--orange); z-index: 3; }
  .skill--vellum { left: 618px; top: 412px; width: 164px; height: 164px; background: var(--purple); z-index: 4; }
  .skill--js { left: 744px; top: 412px; width: 164px; height: 164px; background: var(--pink); z-index: 5; }
  .skill--stack {
    left: 339px; top: 400px; width: 188px; height: 188px; background: var(--green); z-index: 6;
    gap: 5px;
  }
  .tag-row { display: flex; gap: 6px; }
  .tag {
    background: rgba(255,255,255,0.16); border-radius: 14px; padding: 3px 10px;
    font-size: 15px; line-height: 18px;
  }
  .mark { width: 44px; height: 44px; border-radius: 50%; background: rgba(255,255,255,0.28); }
  .nav {
    position: absolute; left: 0; top: 594px; width: 1200px; height: 81px;
    border-top: 1px solid #fbfbfb; background: rgba(226,225,225,0.55);
  }
  .nav__about {
    position: absolute; left: 116px; top: 32px; font-size: 16.5px; color: var(--rust);
    text-decoration: none; letter-spacing: 0.3px;
  }
  .nav__icon { position: absolute; top: 18px; width: 52px; height: 46px; border-radius: 8px; }
  .nav__icon--work { left: 357px; background: #6b6b6b; }
  .nav__icon--blog { left: 594px; background: #e58a5a; border-radius: 50%; width: 46px; }
  .nav__icon--media { left: 792px; background: #4a4a4a; }
  .nav__icon--contact { left: 956px; background: #5a5a5a; border-radius: 50%; width: 64px; }
</style>
</head>
<body>
<div class="canvas">
  <svg class="backdrop" width="1200" height="675" viewBox="0 0 1200 675" aria-hidden="true">
    <path d="M0 494 Q220 470 430 520 Q560 470 700 470 Q900 470 1200 500 L1200 675 L0 675 Z" fill="var(--hill)"/>
    <path d="M260 675 Q360 600 520 560 Q620 600 430 675 Z" fill="#ebeaea"/>
    <ellipse cx="1480" cy="400" rx="552" ry="720" fill="var(--arc-outer)"/>
    <ellipse cx="1500" cy="460" rx="510" ry="700" fill="var(--arc-inner)"/>
  </svg>

  <h1 class="name">Jhon Doe</h1>
  <p class="intro">I'm a Front End Developer and UI Designer based in Toronto. I have a passion for creating clean, beautiful, interactive, responsive and user-friendly UI, developed by modular, scalable and functional code. My freelance work began in 2009, ever since I've been keeping up with the cutting-edge web technologies, aiming to produce a work that I can be proud of.</p>

  <div class="skills">
    <div class="skill skill--awards">
      <svg width="40" height="48" viewBox="0 0 40 48" aria-hidden="true">
        <path d="M4 0h10l6 14 6-14h10l-9 20H13z" fill="rgba(255,255,255,0.35)"/>
        <circle cx="20" cy="32" r="14" fill="rgba(255,255,255,0.35)"/>
        <path d="M20 24l2.4 5 5.4.5-4 3.6 1.2 5.3L20 35.6l-5 2.8 1.2-5.3-4-3.6 5.4-.5z" fill="var(--blue)"/>
      </svg>
      <span class="label">Awards</span>
    </div>
    <div class="skill skill--web">
      <svg width="52" height="44" viewBox="0 0 52 44" aria-hidden="true">
        <rect x="2" y="2" width="42" height="30" rx="3" fill="none" stroke="rgba(255,255,255,0.4)" stroke-width="4"/>
        <rect x="12" y="34" width="18" height="4" fill="rgba(255,255,255,0.4)"/>
        <rect x="34" y="16" width="16" height="26" rx="2" fill="var(--cyan)" stroke="rgba(255,255,255,0.4)" stroke-width="3"/>
      </svg>
      <span class="label">Web Techs</span>
    </div>
    <div class="skill skill--stack">
      <div class="tag-row"><span class="tag">HTML5</span><span class="tag">Canvas</span></div>
      <div class="tag-row"><span class="tag">W3C Standards</span></div>
      <div class="tag-row"><span class="tag">SVG</span><span class="tag">SEO</span></div>
      <div class="tag-row"><span class="tag">Audio/Video</span></div>
    </div>
    <div class="skill skill--css"><span class="mark"></span><span class="label">CSS</span></div>
    <div class="skill skill--vellum"><span class="mark"></span><span class="label">Vellum JS</span></div>
    <div class="skill skill--js"><span class="mark"></span><span class="label">JavaScript</span></div>
  </div>

  <nav class="nav">
    <a class="nav__about" href="#about">ABOUT ME</a>
    <span class="nav__icon nav__icon--work" role="img" aria-label="Hand-drawn television icon for Projects"></span>
    <span class="nav__icon nav__icon--blog" role="img" aria-label="Personal logo mark for Blog"></span>
    <span class="nav__icon nav__icon--media" role="img" aria-label="Hand-drawn film roll icon for Work"></span>
    <span class="nav__icon nav__icon--contact" role="img" aria-label="Hand-lettered hello speech bubble for Contact"></span>
  </nav>
</div>
</body>
</html>
```